Business card design needed

I am a small start up business in the mortgage broking industry based in Sydney called 'nest2keys'. I will be providing residential mortgages to first home owners, investors and people looking to refinance. I would like to see designs that use the colors blue, black, and white - same as my logo (see logo design uploaded)

Target Market(s)

My target market is First Home Owners, property investors, and people looking to refinance. The loans I will be providing are for residential property only at this stage, and my clients will predominantly be in the 30-50yr age bracket.

Industry/Entity Type

Residential

Contact Information for Business Card

Owen Presley
Director/Mobile Mortgage Broker
nests2keys
PO BOX 2984
West Calder NSW 2175
Mb: 0471 286 904
email: owen@brickvaleplex.com.au

Requirements
Must have
• please use lower case for business name (i.e. nests2keys)

```html
<!DOCTYPE html>
<html lang="en">
<head>
<meta charset="utf-8">
<title>nest2keys business card</title>
<link href="https://fonts.googleapis.com/css2?family=Varela+Round&display=swap" rel="stylesheet">
<style>
  :root {
    --page: #ffffff;
    --card: #000000;
    --ink: #ffffff;
    --brand-blue: #3f6db4;
  }
  html, body {
    margin: 0;
    padding: 0;
    width: 1200px;
    height: 1000px;
    overflow: hidden;
    background: var(--page);
    font-family: "Varela Round", sans-serif;
  }
  .canvas {
    position: relative;
    width: 1200px;
    height: 1000px;
  }
  .card {
    position: absolute;
    left: 245px;
    width: 708px;
    height: 437px;
    background: var(--card);
    color: var(--ink);
  }
  .card--front { top: 54px; }
  .card--back { top: 500px; height: 436px; }
  .accent { color: var(--brand-blue); }

  .contact {
    position: absolute;
    right: 22px;
    top: 17px;
    text-align: right;
    font-size: 18px;
    line-height: 21px;
    letter-spacing: -0.2px;
  }
  .identity {
    position: absolute;
    left: 12px;
    top: 158px;
    font-size: 21px;
    letter-spacing: -0.2px;
  }
  .wordmark {
    position: absolute;
    color: var(--brand-blue);
    line-height: 1;
    letter-spacing: -1px;
    white-space: nowrap;
  }
  .card--front .wordmark {
    right: 30px;
    top: 282px;
    font-size: 50px;
  }
  .card--back .wordmark {
    left: 0;
    right: 0;
    text-align: center;
    top: 200px;
    font-size: 64px;
  }
  .postal {
    position: absolute;
    right: 22px;
    top: 397px;
    font-size: 18px;
    letter-spacing: -0.2px;
  }
</style>
</head>
<body>
<div class="canvas">
  <section class="card card--front">
    <div class="contact">
      <div>Mb: <span class="accent">0471 286 904</span></div>
      <div>email: <span class="accent">owen@brickvaleplex.com.au</span></div>
    </div>
    <div class="identity">Owen Presley <span class="accent">Director/Mobile Mortgage Broker</span></div>
    <div class="wordmark">nest2keys</div>
    <div class="postal">nests2keys PO BOX 2984 West Calder NSW 2175</div>
  </section>

  <section class="card card--back">
    <div class="wordmark">nest2keys</div>
  </section>
</div>
</body>
</html>
```